Lumo Brew Premium Matcha brand Label

This is a label design project for a luxury tea brand. Feel free to be creative within the guidelines.
Attached to this project is a document called “Private Label Design Requirements” with the design guidelines and template. There is another document called "Lumo Brew Packaging Instructions" this has more details necessary to stick to the guidelines in the first document.

I have also attached the certifications to be included as well as different variations of the logo for you to use.

If you have any questions, I am here.
Updates

Target Market(s)

Young, active, fun, enjoy the finer things

```html
<!DOCTYPE html>
<html lang="en">
<head>
<meta charset="utf-8">
<title>Lumo Brew Ceremonial Matcha Label</title>
<link rel="stylesheet" href="https://fonts.googleapis.com/css2?family=Oswald:wght@300;400&family=Questrial&display=swap">
<style>
  :root {
    --page-bg: #e4f1d6;
    --label-dark: #232323;
    --label-dark-soft: #2e2e2e;
    --matcha-green: #8ee61c;
    --text-light: #f2f2f2;
    --badge-blue: #3f6fb6;
    --badge-white: #f4f4f4;
  }
  html, body {
    margin: 0;
    width: 1200px;
    height: 800px;
    overflow: hidden;
    background: var(--page-bg);
  }
  .canvas {
    position: relative;
    width: 1200px;
    height: 800px;
  }
  .label {
    position: absolute;
    left: 30px;
    top: 304px;
    width: 1140px;
    height: 192px;
    background: var(--label-dark);
    font-family: "Questrial", "Century Gothic", sans-serif;
    color: var(--text-light);
  }
  .label-texture {
    position: absolute;
    left: 0; top: 0;
    width: 100%;
    height: 153px;
    background: linear-gradient(100deg, var(--label-dark) 0%, var(--label-dark-soft) 45%, var(--label-dark) 100%);
  }
  .label-band {
    position: absolute;
    left: 0; bottom: 0;
    width: 100%;
    height: 39px;
    background: var(--matcha-green);
  }
  .distributor {
    position: absolute;
    left: 59px;
    top: 19px;
    font-size: 13px;
    line-height: 18px;
  }
  .green-heading {
    color: var(--matcha-green);
    font-style: italic;
    font-size: 14px;
  }
  .origin {
    margin-top: 6px;
  }
  .cert-badges {
    position: absolute;
    left: 60px;
    top: 107px;
    display: flex;
    gap: 26px;
    align-items: center;
  }
  .badge-square {
    width: 32px;
    height: 32px;
    background: var(--badge-blue);
  }
  .badge-circle {
    width: 34px;
    height: 34px;
    border-radius: 50%;
    background: var(--badge-white);
  }
  .brand-center {
    position: absolute;
    left: 0;
    width: 100%;
    top: 22px;
    text-align: center;
  }
  .brand-name {
    font-size: 13px;
    color: var(--text-light);
  }
  .product-line {
    margin-top: 10px;
    font-family: "Oswald", "Arial Narrow", sans-serif;
    font-weight: 300;
    font-size: 24px;
    letter-spacing: 1.5px;
    line-height: 28px;
  }
  .product-name {
    font-family: "Oswald", "Arial Narrow", sans-serif;
    font-weight: 400;
    font-size: 30px;
    letter-spacing: 1.5px;
    line-height: 36px;
    color: var(--matcha-green);
  }
  .net-weight {
    position: absolute;
    bottom: 0;
    left: 0;
    width: 100%;
    height: 39px;
    line-height: 39px;
    text-align: center;
    font-size: 14px;
    color: var(--text-light);
  }
  .directions {
    position: absolute;
    left: 861px;
    top: 20px;
    font-size: 12px;
    line-height: 14px;
  }
  .directions .green-heading {
    font-size: 13px;
  }
  .steps {
    list-style: none;
    margin: 2px 0 0;
    padding: 0;
  }
  .steps li {
    position: relative;
    padding-left: 16px;
  }
  .steps li::before {
    content: "";
    position: absolute;
    left: 3px;
    top: 4px;
    width: 5px;
    height: 5px;
    background: var(--matcha-green);
    border-radius: 0 5px 0 5px;
  }
  .storage-note {
    position: absolute;
    left: 861px;
    bottom: 0;
    height: 39px;
    line-height: 39px;
    font-family: "Oswald", "Arial Narrow", sans-serif;
    font-size: 12px;
    letter-spacing: 1px;
    color: var(--text-light);
  }
</style>
</head>
<body>
<div class="canvas">
  <section class="label">
    <div class="label-texture" role="img" aria-label="Dark charcoal background with fine flowing wave lines"></div>
    <div class="label-band"></div>

    <div class="distributor">
      <div class="green-heading">Distributed by</div>
      <div>Lumo Brew Co. | Atlanta, Ga</div>
      <div>Certified Organic by Verdan</div>
      <div class="origin">PRODUCT OF JAPAN</div>
    </div>

    <div class="cert-badges">
      <div class="badge-square" role="img" aria-label="Non-GMO certification badge"></div>
      <div class="badge-circle" role="img" aria-label="Organic certification badge"></div>
    </div>

    <div class="brand-center">
      <div class="brand-name">Lumo Brew</div>
      <div class="product-line">PREMIUM ORGANIC</div>
      <div class="product-name">CEREMONIAL MATCHA</div>
    </div>

    <div class="net-weight">Net Wt: 30g (1.06oz)</div>

    <div class="directions">
      <div class="green-heading">Ingredients:</div>
      <div>Premium Organic Japanese</div>
      <div>Matcha Green Tea</div>
      <div class="green-heading">Instructions:</div>
      <ul class="steps">
        <li>2 tsp of Matcha</li>
        <li>2oz of Water (170-180 degrees F)</li>
        <li>Whisk in a W formation until frothy</li>
        <li>Sweeten to taste</li>
      </ul>
    </div>

    <div class="storage-note">KEEP REFRIGERATED FOR QUALITY</div>
  </section>
</div>
</body>
</html>
```